Belford & Company

We are a boutique commercial real estate firm. For our Business card design - sleek, modern, yet high-end/classy. Please see our website: belfordandcompany.example for details.

We currently need 2 business card names and the ability to add/change the business card information -
Name, Title, Address, Office #, Mobile #, Fax, Email and company website.

Industry/Entity Type

Real Estate

Contact Information for Business Card

Business card design - sleek, modern, yet high-end/classy. Please see our website: belfordandcompany.example for details.

Also, we'd like to have our slogan "Precision Builds Lasting Value." somewhere in there. We'd like to make some part of it raised or a different texture if possible.
Color #'s:
blue 19 36 128
light gray 222 222 221
dark gray 107 120 128

Also, we'd like to have our slogan "Precision Builds Lasting Value." somewhere in there. We'd like to make some part of it raised or a different texture if possible - grey on one side and blue on the other - rounded edges preferred. Maybe either metal/silver/grey raised logo on the back. Thank you!!

Requirements
Must have
• Sleek, modern, clean and classy design

```html
<!DOCTYPE html>
<html lang="en">
<head>
<meta charset="utf-8">
<title>Belford &amp; Company — Business Card</title>
<link href="https://fonts.googleapis.com/css2?family=Prompt:wght@400;500;600;700&display=swap" rel="stylesheet">
<style>
  :root {
    --stage-green: #9aca3c;
    --brand-blue: #132480;
    --mid-blue: #3350a0;
    --dark-gray: #6b7880;
    --light-gray: #dededd;
    --pale-text: #e4e7ea;
    --white: #ffffff;
  }
  * { box-sizing: border-box; margin: 0; padding: 0; }
  html, body { width: 1200px; height: 1200px; overflow: hidden; }
  body {
    background: var(--stage-green);
    font-family: "Prompt", sans-serif;
    position: relative;
  }
  .card {
    position: absolute;
    left: 150px;
    width: 900px;
    height: 540px;
    border-radius: 40px;
    overflow: hidden;
  }
  .card--front { top: 46px; background: var(--dark-gray); }
  .card--back {
    top: 614px;
    background: linear-gradient(120deg, #18287f 0%, #2a3a82 40%, #3b4c82 78%, #5d6a86 100%);
  }
  .tower-art {
    position: absolute;
    background: linear-gradient(90deg, rgba(255,255,255,0.06), rgba(255,255,255,0.16));
  }
  .card--front .tower-art { right: 0; top: 0; width: 70px; height: 430px; }
  .card--back .tower-art {
    left: 0; top: 6px; width: 390px; height: 534px;
    background: linear-gradient(100deg, rgba(80,100,180,0.45) 0%, rgba(60,80,170,0.18) 55%, rgba(60,80,170,0) 100%);
  }
  .wordmark {
    position: absolute;
    display: flex;
    align-items: center;
    gap: 14px;
    color: var(--white);
    font-weight: 600;
    line-height: 1;
  }
  .wordmark__square {
    width: 22px; height: 22px;
    background: var(--white);
    flex: none;
  }
  .wordmark__name { display: flex; flex-direction: column; gap: 6px; }
  .card--front .wordmark { left: 94px; top: 150px; font-size: 40px; }
  .card--back .wordmark { left: 290px; top: 215px; font-size: 50px; }
  .person { position: absolute; left: 504px; top: 192px; }
  .person__name {
    color: var(--brand-blue);
    font-weight: 700;
    font-size: 35px;
    line-height: 1;
    letter-spacing: 0.3px;
  }
  .person__title { color: var(--light-gray); font-size: 17px; font-weight: 500; margin-top: 2px; }
  .divider {
    position: absolute; left: 94px; top: 293px; width: 716px; height: 3px;
    background: linear-gradient(90deg, rgba(222,222,221,0), var(--light-gray) 12%, var(--light-gray) 85%, rgba(222,222,221,0));
  }
  .contact {
    position: absolute; top: 320px;
    color: var(--pale-text);
    font-size: 19px; font-weight: 500;
    line-height: 31px;
    list-style: none;
  }
  .contact--left { left: 90px; }
  .contact--right { right: 100px; text-align: right; }
  .contact li { display: flex; align-items: center; gap: 14px; height: 31px; }
  .contact--right li { justify-content: flex-end; }
  .contact__icon { width: 20px; height: 20px; flex: none; }
  .contact__spacer { width: 20px; flex: none; }
  .band { position: absolute; left: 0; top: 430px; width: 900px; height: 110px; }
  .slogan {
    position: absolute; right: 88px; top: 476px;
    color: var(--brand-blue); font-weight: 600; font-size: 18px;
  }
</style>
</head>
<body>

<section class="card card--front" aria-label="Business card front">
  <div class="tower-art" role="img" aria-label="Faint stylised office tower decoration"></div>

  <div class="wordmark">
    <span class="wordmark__square"></span>
    <span class="wordmark__name"><span>BELFORD</span><span>&amp; COMPANY</span></span>
  </div>

  <div class="person">
    <div class="person__name">MARCUS HALDEN</div>
    <div class="person__title">Managing Director</div>
  </div>

  <div class="divider"></div>

  <ul class="contact contact--left">
    <li>
      <svg class="contact__icon" viewBox="0 0 20 20"><circle cx="10" cy="10" r="8.5" fill="none" stroke="#132480" stroke-width="2"/><path d="M2 10h16M10 1.5c3 3 3 14 0 17M10 1.5c-3 3-3 14 0 17" fill="none" stroke="#132480" stroke-width="1.4"/></svg>
      <span>www.belfordandcompany.example</span>
    </li>
    <li>
      <svg class="contact__icon" viewBox="0 0 20 20"><path d="M10 1a6 6 0 0 1 6 6c0 4.5-6 12-6 12S4 11.5 4 7a6 6 0 0 1 6-6z" fill="#132480"/><circle cx="10" cy="7" r="2.2" fill="#6b7880"/></svg>
      <span>2285 Harbor View Ave., Suite #310</span>
    </li>
    <li><span class="contact__spacer"></span><span>Riverton, FL 32000</span></li>
  </ul>

  <ul class="contact contact--right">
    <li>
      <span>(555) 014-2278</span>
      <svg class="contact__icon" viewBox="0 0 20 20"><rect x="5" y="1" width="10" height="18" rx="2" fill="none" stroke="#132480" stroke-width="1.8"/><line x1="8.5" y1="16" x2="11.5" y2="16" stroke="#132480" stroke-width="1.5"/></svg>
    </li>
    <li>
      <span>(555) 017-3390</span>
      <svg class="contact__icon" viewBox="0 0 20 20"><path d="M2 7c0-3 16-3 16 0v1.5h-4V6.5H6v2H2z" fill="#132480"/><rect x="4" y="10" width="12" height="8" rx="1" fill="none" stroke="#132480" stroke-width="1.6"/><circle cx="10" cy="13.5" r="1.8" fill="#132480"/></svg>
    </li>
    <li>
      <span>info@belfordandcompany.example</span>
      <svg class="contact__icon" viewBox="0 0 20 20"><rect x="1" y="4" width="18" height="13" rx="1.5" fill="#132480"/><path d="M2 5.5l8 6 8-6" fill="none" stroke="#6b7880" stroke-width="1.6"/></svg>
    </li>
  </ul>

  <svg class="band" viewBox="0 0 900 110" preserveAspectRatio="none" aria-hidden="true">
    <rect x="0" y="0" width="900" height="10" fill="#132480"/>
    <polygon points="0,10 362,10 302,110 0,110" fill="#132480"/>
    <polygon points="466,23 900,23 900,45 455,45" fill="#3350a0"/>
    <polygon points="402,45 900,45 900,110 364,110" fill="#dededd"/>
  </svg>
  <div class="slogan">Precision Builds Lasting Value</div>
</section>

<section class="card card--back" aria-label="Business card back">
  <div class="tower-art" role="img" aria-label="Large faint office tower decoration"></div>
  <div class="wordmark">
    <span class="wordmark__square"></span>
    <span class="wordmark__name"><span>BELFORD</span><span>&amp; COMPANY</span></span>
  </div>
</section>

</body>
</html>
```